New Plumbing Company

We are looking for a smart and creative business card design for our new plumbing company. We are looking for creativity and originality in our business cards.

Industry/Entity Type

Plumbing

Contact Information for Business Card

Crestline Plumbing
Peter Halvane
Managing Director
Telephone Number : 0481529604
Email : service@crestlineplumbing.com.au
Website : www.crestlineplumbing.com.au
Lic. 508264K

Colors
0692cd
33a6d7
000000

Requirements
Must have
• I want the business card to be designed on a black background using the blue tones i have selected as seen in the company logo.

```html
<!DOCTYPE html>
<html lang="en">
<head>
<meta charset="utf-8">
<title>Crestline Plumbing – Business Cards</title>
<link href="https://fonts.googleapis.com/css2?family=Montserrat:wght@300;400;500&display=swap" rel="stylesheet">
<style>
  :root {
    --brand-blue: #0692cd;
    --brand-blue-light: #33a6d7;
    --card-black: #000000;
    --card-charcoal: #1c1d1f;
    --backdrop: #ececec;
    --text-white: #ffffff;
    --text-grey: #c9cbce;
    --text-muted: #9a9da1;
  }
  * { box-sizing: border-box; margin: 0; padding: 0; }
  html, body {
    width: 1200px; height: 779px; overflow: hidden;
    background: var(--backdrop);
    font-family: "Montserrat", sans-serif;
  }
  .canvas {
    position: relative; width: 1200px; height: 779px;
    display: flex; align-items: center; justify-content: center; gap: 40px;
  }
  .card {
    position: relative; width: 540px; height: 300px; overflow: hidden;
    background: radial-gradient(ellipse at 45% 40%, var(--card-charcoal) 0%, var(--card-black) 85%);
    box-shadow: 0 14px 30px rgba(0,0,0,0.22);
  }
  /* Logo side */
  .brand-lockup {
    position: absolute; inset: 0;
    display: flex; align-items: center; justify-content: center; gap: 16px;
  }
  .brand-mark {
    width: 40px; height: 40px; border-radius: 50%;
    background: var(--brand-blue);
  }
  .brand-name {
    font-weight: 400; font-size: 30px; letter-spacing: 0.5px;
    color: var(--text-white);
  }
  /* Contact side */
  .card-shape { position: absolute; inset: 0; }
  .panel-lockup {
    position: absolute; left: 24px; top: 118px;
    display: flex; align-items: center; gap: 10px;
  }
  .panel-lockup .brand-mark {
    width: 28px; height: 28px; background: none; border: 2px solid var(--text-white);
  }
  .panel-lockup .brand-name { font-size: 19px; }
  .person {
    position: absolute; right: 30px; top: 34px; text-align: right;
  }
  .person-name {
    font-weight: 300; font-size: 28px; color: var(--brand-blue-light); letter-spacing: 0.3px;
  }
  .person-role {
    font-weight: 300; font-size: 16px; color: var(--text-grey); margin-top: 2px;
  }
  .person-licence {
    font-weight: 300; font-size: 10px; color: var(--text-muted); margin-top: 4px;
  }
  .contact-list {
    position: absolute; left: 248px; top: 170px; list-style: none;
  }
  .contact-item {
    display: flex; align-items: center; gap: 14px;
    font-weight: 300; font-size: 11.5px; color: var(--text-grey);
    height: 29px;
  }
  .contact-icon { width: 16px; height: 16px; flex: none; }
</style>
</head>
<body>
<main class="canvas">

  <section class="card card--logo" aria-label="Business card, logo side">
    <div class="brand-lockup">
      <span class="brand-mark"></span>
      <span class="brand-name">Crestline Plumbing</span>
    </div>
  </section>

  <section class="card card--contact" aria-label="Business card, contact side">
    <svg class="card-shape" viewBox="0 0 540 300" width="540" height="300" aria-hidden="true">
      <path d="M0 0 H300 C272 105 258 215 178 300 H0 Z" fill="var(--brand-blue)"/>
      <path d="M304 -2 C276 105 262 218 183 302" fill="none" stroke="var(--text-white)" stroke-width="5"/>
    </svg>

    <div class="panel-lockup">
      <span class="brand-mark"></span>
      <span class="brand-name">Crestline Plumbing</span>
    </div>

    <div class="person">
      <p class="person-name">Peter Halvane</p>
      <p class="person-role">Managing Director</p>
      <p class="person-licence">Lic. 508264K</p>
    </div>

    <ul class="contact-list">
      <li class="contact-item">
        <svg class="contact-icon" viewBox="0 0 16 16" aria-hidden="true">
          <path d="M4 1.5 L6.2 4.6 L4.9 6.2 C5.8 8 7.6 9.9 9.6 11 L11.2 9.7 L14.3 11.9 L13 14.3 C8 14 2 8 1.8 3 Z" fill="var(--text-grey)"/>
        </svg>
        <span>048.152.9604</span>
      </li>
      <li class="contact-item">
        <svg class="contact-icon" viewBox="0 0 16 16" aria-hidden="true">
          <rect x="1" y="3.5" width="14" height="9.5" fill="none" stroke="var(--text-grey)" stroke-width="1.3"/>
          <path d="M1 3.5 L8 9 L15 3.5" fill="none" stroke="var(--text-grey)" stroke-width="1.3"/>
        </svg>
        <span>service@crestlineplumbing.com.au</span>
      </li>
      <li class="contact-item">
        <svg class="contact-icon" viewBox="0 0 16 16" aria-hidden="true">
          <circle cx="8" cy="8" r="6.5" fill="none" stroke="var(--text-grey)" stroke-width="1.3"/>
          <ellipse cx="8" cy="8" rx="2.8" ry="6.5" fill="none" stroke="var(--text-grey)" stroke-width="1.1"/>
          <path d="M1.5 8 H14.5 M2.6 4.7 H13.4 M2.6 11.3 H13.4" stroke="var(--text-grey)" stroke-width="1"/>
        </svg>
        <span>www.crestlineplumbing.com.au</span>
      </li>
    </ul>
  </section>

</main>
</body>
</html>
```